Bright Kestrel Studio - Redesign of our website - needs to be dynamic and alive!

We provide fun lessons exclusively in students' homes in music, art, yoga and acting. I like most of the graphics and copy on the site now, but it looks too static and there might be too much info to read on the home page. Needs movement, needs to generate excitement and be a fun place to visit, yet keeping professional-looking. The site needs better SEO, a better look and needs to generate more business, as several people see it each day but few contact us for details about our program. The site is brightkestrel-studio.test. I'd like it to continue to be hosted on my domain in Wordpress format so I can add and delete teacher photos from time to time. I like the way the teachers' bios currently pop up when a cursor is hovered over them on the Our Team page. Thank you and good luck!

Target Market(s)

Wealthy, college-educated households with children who live in the Greater Atlanta area

Industry/Entity Type

Education

Coding

Number of Pages Required

Requirements
Must have
• Home Page movement, excitement, but keeping it professional-looking. We're an educational company and want to market to people who are looking for a professional yet fun/exciting approach to lessons in their homes.
Nice to have
• The info on the Testimonials page can probably rotate and fade in/fade out on the home page or slide on/slide off instead of having a separate page for these.
• The info on the Trial Lessons page can probably be included as a banner on the home page too instead of being a separate page. Nice if I can change the text on this myself from time to time to mention any promotions I might be offering with regard to trial lessons.

```html
<!DOCTYPE html>
<html lang="en">
<head>
<meta charset="utf-8">
<title>Bright Kestrel Studio – Website Redesign Screens</title>
<link href="https://fonts.googleapis.com/css2?family=Open+Sans:ital,wght@0,400;0,600;0,700;0,800;1,400&family=Roboto+Slab:wght@400;600&display=swap" rel="stylesheet">
<style>
:root{
  --teal:#19a9cf; --green:#b5cf2f; --yellow:#f9d84a; --orange:#f7941d;
  --lavender:#b59ad0; --sky:#9fd8df; --rust:#e96b2c; --purple:#6b3a9a;
  --cta:#b14fd6; --heading-blue:#1a9ad6; --ink:#444; --mute:#777;
  --panel:#f1f5f6;
}
*{box-sizing:border-box;margin:0;padding:0}
html,body{width:1200px;height:960px;overflow:hidden;background:#fff}
body{position:relative;font-family:"Open Sans",sans-serif;color:var(--ink)}
.abs{position:absolute}
.stripes{position:absolute;background:linear-gradient(135deg,#fce9c4 0%,#e7f3d3 30%,#e2eef8 60%,#efe2f6 85%,#fbe5d3 100%)}
.screen{position:absolute;background:#fff;box-shadow:0 2px 10px rgba(0,0,0,.18);overflow:hidden}
.site-header{position:absolute;left:0;top:0;right:0;background:#fff;display:flex;align-items:center;padding-left:var(--pad,48px);box-shadow:0 1px 4px rgba(0,0,0,.12);z-index:2}
.brand{display:flex;align-items:center;gap:3px;font-weight:700;font-size:7px;color:var(--purple);width:62px;line-height:1.05;flex:none}
.brand-dot{width:8px;height:8px;border-radius:50%;background:var(--teal);flex:none}
.nav{display:flex;gap:var(--nav-gap,9px);font-family:"Roboto Slab",serif;font-size:var(--nav-size,5px);color:var(--mute);white-space:nowrap;flex:none}
.nav .current{color:#333;border-bottom:1.5px solid var(--cta);padding-bottom:2px}
.header-right{margin-left:auto;margin-right:var(--pad-r,60px);display:flex;gap:6px;align-items:center;font-size:5px;color:var(--cta);font-weight:600;white-space:nowrap;flex:none}
.soc{width:5px;height:5px;border-radius:1px;background:#888}
.phone-icon{width:6px;height:6px}
.photo{position:absolute}
.btn{position:absolute;background:var(--cta);color:#fff;font-size:4.6px;font-weight:700;display:flex;align-items:center;justify-content:center;box-shadow:0 1px 2px rgba(0,0,0,.2)}
.rule-heading{position:absolute;left:0;right:0;display:flex;align-items:center;gap:10px}
.rule-heading::before,.rule-heading::after{content:"";flex:1;height:2px;background:var(--line,#444)}
.bubble-band{position:absolute;background:linear-gradient(90deg,var(--teal) 0%,var(--green) 20%,var(--yellow) 38%,var(--orange) 52%,var(--sky) 68%,var(--teal) 78%,var(--lavender) 100%)}
.center{text-align:center}
/* courses */
.course-card{position:absolute;background:#fff;box-shadow:0 1px 4px rgba(0,0,0,.2);font-family:"Roboto Slab",serif;overflow:hidden}
.side-card{background:linear-gradient(90deg,#fff,#eef6f8 30%,#fbf3e6 55%,#f3eefa 80%,#fff)}
.side-card span{position:absolute;top:24px;left:4px;right:3px;font-size:4.6px;color:#333;padding-bottom:2px;border-bottom:1.5px solid var(--teal);white-space:nowrap;text-align:center}
.feature-card h4{font-family:"Roboto Slab",serif;font-weight:400;font-size:6px;text-align:center;margin:16px 9px 4px;padding-bottom:3px;border-bottom:1.5px solid var(--purple)}
.feature-card a{display:block;font-family:"Open Sans",sans-serif;font-size:4.3px;font-weight:700;color:#222;text-decoration:underline;margin:4px 9px}
.feature-card p{font-family:"Open Sans",sans-serif;font-size:4.2px;line-height:1.35;margin:4px 9px;color:#333}
.blurb{position:absolute;font-size:4.6px;line-height:1.6;color:#555;text-align:center}
.blurb .link{color:var(--heading-blue)}
/* play */
.play-band{position:absolute;left:0;right:0;top:0;height:33px;background:linear-gradient(180deg,#3570d0,#4e88e0)}
.play-title{font-weight:700;color:var(--green);font-size:10px;--line:var(--green)}
.play-panel{position:absolute;left:0;right:0;top:89px;height:142px;background:#fff;display:grid;grid-template-columns:repeat(4,1fr)}
.subject{position:relative}
.subject h3{font-family:"Open Sans",sans-serif;font-weight:800;text-transform:uppercase;font-size:14px;text-align:center;margin-top:12px;letter-spacing:.3px}
.subject .photo{left:12px;right:12px;top:32px;height:94px;opacity:.35}
.subject.active{box-shadow:0 0 6px rgba(0,0,0,.15)}
.subject.active .photo{opacity:1}
.subject .bar{position:absolute;left:6px;right:6px;top:129px;height:5px;border-radius:3px}
.subject .bar::after{content:"";position:absolute;left:50%;top:-5px;margin-left:-5px;border:5px solid transparent;border-top:0;border-bottom:5px solid #fff}
.subject.active .bar::after{top:5px;border-bottom:0;border-top:5px solid var(--purple)}
.popup{position:absolute;left:6px;right:6px;top:76px;height:58px;background:#d9b1ee;color:#fff;font-size:4.1px;line-height:1.35;text-align:center;padding:5px 5px;border-top:5px solid var(--purple)}
</style>
</head>
<body>

<svg width="0" height="0" style="position:absolute" aria-hidden="true">
  <defs>
    <symbol id="phone" viewBox="0 0 10 10"><path d="M2 1l2 2-1 1.2c.6 1.2 1.5 2.1 2.8 2.8L7 6l2 2-1.2 1.4C4.5 9 1 5.5.6 2.2z" fill="currentColor"/></symbol>
  </defs>
</svg>

<!-- ========== Home: trial lesson + testimonials ========== -->
<div class="stripes" style="left:0;top:68px;width:404px;height:374px" role="img" aria-label="Diagonal multicolour confetti stripe pattern"></div>
<div class="screen" style="left:0;top:32px;width:405px;height:36px;overflow:visible;box-shadow:none">
  <header class="site-header" style="height:36px;--pad:48px;--pad-r:46px">
    <div class="brand"><span class="brand-dot"></span>Bright Kestrel Studio</div>
    <nav class="nav" style="margin-left:14px"><span>Home</span><span>About Us</span><span class="current">Courses</span><span>Programs</span><span>Gallery</span><span>Contact Us</span></nav>
    <div class="header-right"><span class="soc"></span><span class="soc"></span><svg class="phone-icon"><use href="#phone"/></svg>(555) 010-4477</div>
  </header>
</div>
<main class="screen" style="left:29px;top:68px;width:347px;height:342px">
  <section class="trial-banner abs" style="left:0;top:0;width:347px;height:162px;background:#fff">
    <h2 class="abs center" style="left:40px;right:40px;top:30px;font-size:8.4px;line-height:1.3;color:var(--heading-blue);font-weight:700">Why not take a trial lesson or two and see what the Bright Kestrel Studio experience is all about?</h2>
    <p class="abs center" style="left:70px;right:70px;top:56px;font-family:'Roboto Slab',serif;font-size:5.4px;line-height:1.5;color:var(--purple)">Try a lesson with one of our teachers in your home, and then decide if our program is right for you.</p>
    <div class="photo" style="left:19px;top:76px;width:64px;height:66px;background:linear-gradient(180deg,#fff 0%,#e3bfa3 35%,#9a7f6e 70%,#fff 100%)" role="img" aria-label="Photo of a young gymnast in a stretching yoga pose"></div>
    <div class="photo" style="left:275px;top:76px;width:48px;height:86px;background:linear-gradient(180deg,#fff 0%,#e9c9a8 22%,#f7941d 45%,#f37d12 100%)" role="img" aria-label="Photo of a smiling girl in an orange top"></div>
    <p class="abs center" style="left:110px;right:110px;top:98px;font-family:'Roboto Slab',serif;font-size:3.8px;line-height:1.55;color:#555">A trial lesson does not commit you to register for the remainder of the season, and you only pay for the trial lesson (or two) you received. This is an excellent way to help you decide if you'd like to be part of our program!</p>
    <p class="abs center" style="left:90px;right:90px;top:133px;font-size:3.8px;color:#555">Call us at (555) 010-4477 or e-mail us to arrange your first lesson.</p>
    <div class="btn" style="left:98px;top:146px;width:63px;height:10px">Call us at (555) 010-4477</div>
    <span class="abs" style="left:170px;top:145px;font-family:'Roboto Slab',serif;font-size:6px">or</span>
    <div class="btn" style="left:185px;top:146px;width:63px;height:10px">e-mail us</div>
  </section>
  <section class="testimonials abs" style="left:0;top:164px;width:347px;height:140px;background:var(--panel)">
    <h2 class="rule-heading" style="top:14px;font-size:10.5px;font-weight:700;color:var(--purple);--line:var(--purple)">Testimonials</h2>
    <blockquote class="abs center" style="left:100px;right:100px;top:56px;font-style:italic;font-size:5.4px;line-height:1.45;color:#444">“I can't say enough about how wonderful I think the Bright Kestrel Studio program is. Our teacher makes learning a joy; I never have to ask my kids to practice.”</blockquote>
    <cite class="abs center" style="left:0;right:0;top:88px;font-style:normal;font-weight:700;font-size:5.6px">- Hollowreed Reviews</cite>
    <svg class="abs" style="left:40px;top:68px" width="6" height="8" viewBox="0 0 6 8"><path d="M5 0L1 4l4 4" fill="none" stroke="#555"/></svg>
    <svg class="abs" style="left:303px;top:68px" width="6" height="8" viewBox="0 0 6 8"><path d="M1 0l4 4-4 4" fill="none" stroke="#555"/></svg>
    <div class="bubble-band" style="left:0;top:106px;width:347px;height:34px" role="img" aria-label="Colourful scalloped bubble border ornament"></div>
  </section>
  <footer class="abs" style="left:0;top:304px;width:347px;height:38px;background:var(--panel)">
    <div class="abs" style="left:168px;top:6px;width:12px;height:12px;background:var(--cta);border-radius:1px" aria-label="Back to top"><svg width="12" height="12" viewBox="0 0 12 12"><path d="M4 7l2-2 2 2" fill="none" stroke="#fff"/></svg></div>
    <p class="abs center" style="left:0;right:0;top:26px;font-size:4.6px;color:#555">© 2017 Bright Kestrel Studio, Inc. All rights reserved.</p>
  </footer>
</main>

<!-- ========== Courses carousel ========== -->
<div class="stripes" style="left:404px;top:140px;width:796px;height:300px" role="img" aria-label="Diagonal multicolour confetti stripe pattern"></div>

<section class="screen" style="left:433px;top:158px;width:341px;height:282px">
  <header class="site-header" style="height:34px;--pad:26px;--pad-r:20px;--nav-gap:7px;--nav-size:4.6px">
    <div class="brand"><span class="brand-dot"></span>Bright Kestrel Studio</div>
    <nav class="nav" style="margin-left:6px"><span>Home</span><span>About Us</span><span class="current">Courses</span><span>Programs</span><span>Gallery</span><span>Contact Us</span></nav>
    <div class="header-right"><span class="soc"></span><span class="soc"></span><svg class="phone-icon"><use href="#phone"/></svg>(555) 010-4477</div>
  </header>
  <div class="abs" style="left:0;top:34px;width:341px;height:248px;background:var(--panel)"></div>
  <h2 class="rule-heading" style="top:51px;font-family:'Roboto Slab',serif;font-size:6px;font-weight:600;color:#333">Courses</h2>
  <div class="course-card side-card" style="left:17px;top:80px;width:50px;height:110px;transform:skewY(4deg)"><span>Music Lessons</span></div>
  <div class="course-card side-card" style="left:60px;top:78px;width:50px;height:114px;transform:skewY(3deg)"><span>Music Workshops</span></div>
  <div class="course-card side-card" style="left:232px;top:78px;width:50px;height:114px;transform:skewY(-3deg)"><span style="border-color:var(--green)">Visual Art Lessons</span></div>
  <div class="course-card side-card" style="left:276px;top:80px;width:50px;height:110px;transform:skewY(-4deg)"><span style="border-color:var(--orange)">Yoga Classes</span></div>
  <article class="course-card feature-card" style="left:107px;top:76px;width:128px;height:114px">
    <div class="bubble-band" style="left:0;top:0;width:128px;height:9px" role="img" aria-label="Colourful bubble border ornament"></div>
    <h4>Acting Lessons</h4>
    <a>Acting Foundations</a>
    <p>Ideal for young actors (7-10 yrs.) looking for a fun introduction to theater. Use of theater games and exercises to explore character, improvisation, voice, and movement. A great first acting class for building skills and confidence.</p>
    <a>Performance Techniques</a>
    <a>Personal Coaching</a>
    <div class="bubble-band" style="left:0;top:105px;width:128px;height:9px" role="img" aria-label="Colourful bubble border ornament"></div>
  </article>
  <div class="bubble-band" style="left:0;top:214px;width:341px;height:24px" role="img" aria-label="Colourful scalloped bubble border ornament"></div>
  <p class="blurb" style="left:18px;right:18px;top:248px">Bright Kestrel Studio is continually adding new subjects and workshops to its list of courses, responding to the diverse needs and requests of its clients. These are the courses we currently offer instruction in to children, teens and adults, all taught in-home</p>
  <div class="btn" style="left:146px;top:272px;width:50px;height:10px">Our Programs</div>
</section>

<section class="screen" style="left:830px;top:158px;width:342px;height:282px">
  <header class="site-header" style="height:34px;--pad:26px;--pad-r:20px;--nav-gap:7px;--nav-size:4.6px">
    <div class="brand"><span class="brand-dot"></span>Bright Kestrel Studio</div>
    <nav class="nav" style="margin-left:6px"><span>Home</span><span>About Us</span><span class="current">Courses</span><span>Programs</span><span>Gallery</span><span>Contact Us</span></nav>
    <div class="header-right"><span class="soc"></span><span class="soc"></span><svg class="phone-icon"><use href="#phone"/></svg>(555) 010-4477</div>
  </header>
  <div class="abs" style="left:0;top:34px;width:342px;height:248px;background:var(--panel)"></div>
  <h2 class="rule-heading" style="top:51px;font-family:'Roboto Slab',serif;font-size:6px;font-weight:600;color:#333">Courses</h2>
  <div class="course-card side-card" style="left:15px;top:80px;width:50px;height:110px;transform:skewY(4deg)"><span>Music Lessons</span></div>
  <div class="course-card side-card" style="left:188px;top:78px;width:50px;height:114px;transform:skewY(-3deg)"><span style="border-color:var(--purple)">Acting Lessons</span></div>
  <div class="course-card side-card" style="left:232px;top:78px;width:50px;height:114px;transform:skewY(-3deg)"><span style="border-color:var(--green)">Visual Art Lessons</span></div>
  <div class="course-card side-card" style="left:277px;top:80px;width:50px;height:110px;transform:skewY(-4deg)"><span style="border-color:var(--orange)">Yoga Classes</span></div>
  <article class="course-card feature-card" style="left:59px;top:76px;width:128px;height:114px">
    <div class="bubble-band" style="left:0;top:0;width:128px;height:9px" role="img" aria-label="Colourful bubble border ornament"></div>
    <h4 style="border-color:var(--teal)">Music Workshops</h4>
    <a>All Together Now</a>
    <a>Artist Development</a>
    <a>Recording Arts</a>
    <a>Early/Late Lessons</a>
    <p>Open to music students able to schedule lesson time during weekdays beginning after 8:15 pm or ending by 2:45 pm. Lessons may (but do not have</p>
    <div class="abs" style="right:8px;top:30px;width:2px;height:36px;background:#ddd"><div style="height:16px;background:var(--teal)"></div></div>
    <div class="bubble-band" style="left:0;top:105px;width:128px;height:9px" role="img" aria-label="Colourful bubble border ornament"></div>
  </article>
  <div class="bubble-band" style="left:0;top:214px;width:342px;height:24px" role="img" aria-label="Colourful scalloped bubble border ornament"></div>
  <p class="blurb" style="left:18px;right:18px;top:248px">Bright Kestrel Studio is continually adding new subjects and workshops to its list of courses, responding to the diverse needs and requests of its clients. These are the courses we currently offer instruction in to children, teens and adults, all taught in-home</p>
  <div class="btn" style="left:146px;top:272px;width:50px;height:10px">Our Programs</div>
</section>

<!-- ========== It's Time To Play ========== -->
<div class="stripes" style="left:0;top:571px;width:1200px;height:285px" role="img" aria-label="Diagonal multicolour confetti stripe pattern"></div>

<!-- state 1: default -->
<section class="screen" style="left:29px;top:571px;width:343px;height:285px;box-shadow:none;background:var(--panel)">
  <div class="play-band" role="img" aria-label="Blue banner with illustrated drum and electric guitar"></div>
  <h2 class="rule-heading play-title" style="top:43px">It's Time To Play!</h2>
  <div class="bubble-band" style="left:0;top:65px;width:343px;height:24px" role="img" aria-label="Colourful scalloped bubble border ornament"></div>
  <div class="play-panel">
    <div class="subject"><h3 style="color:var(--teal)">Music</h3><div class="photo" style="background:linear-gradient(180deg,#fff,#e6a08c 40%,#c86a3a 70%,#9ab0c8)" role="img" aria-label="Photo of a boy playing electric guitar"></div><div class="bar" style="background:var(--teal)"></div></div>
    <div class="subject"><h3 style="color:var(--purple)">Theater</h3><div class="photo" style="background:linear-gradient(180deg,#fff,#8bd35a 35%,#2c2c2c 70%,#fff)" role="img" aria-label="Photo of a performer in green shirt and suspenders"></div><div class="bar" style="background:var(--purple)"></div></div>
    <div class="subject"><h3 style="color:var(--green)">Art</h3><div class="photo" style="background:linear-gradient(180deg,#fff,#c69a7a 35%,#b83a2c 65%,#e8e2dc)" role="img" aria-label="Photo of a child holding paintbrushes"></div><div class="bar" style="background:var(--green)"></div></div>
    <div class="subject"><h3 style="color:var(--orange)">Yoga</h3><div class="photo" style="background:linear-gradient(180deg,#fff,#d9b49a 45%,#9a9a9a 75%,#fff)" role="img" aria-label="Photo of a girl in a yoga pose"></div><div class="bar" style="background:var(--orange)"></div></div>
  </div>
  <div class="bubble-band" style="left:0;top:231px;width:343px;height:26px" role="img" aria-label="Colourful scalloped bubble border ornament"></div>
  <p class="blurb" style="left:30px;right:30px;top:266px">We are happy to arrange a trial lesson in all subjects we offer instruction in, just call us at <span class="link">(555) 010-4477</span><br>or <span class="link">email us</span> via the Contact page and we will find a day and time that is convenient for you.</p>
</section>

<!-- state 2: hover -->
<section class="screen" style="left:429px;top:571px;width:343px;height:285px;box-shadow:none;background:var(--panel)">
  <div class="play-band" role="img" aria-label="Blue banner with illustrated drum and electric guitar"></div>
  <h2 class="rule-heading play-title" style="top:43px">It's Time To Play!</h2>
  <div class="bubble-band" style="left:0;top:65px;width:343px;height:24px" role="img" aria-label="Colourful scalloped bubble border ornament"></div>
  <div class="play-panel">
    <div class="subject"><h3 style="color:var(--teal)">Music</h3><div class="photo" style="background:linear-gradient(180deg,#fff,#e6a08c 40%,#c86a3a 70%,#9ab0c8)" role="img" aria-label="Photo of a boy playing electric guitar"></div><div class="bar" style="background:var(--teal)"></div></div>
    <div class="subject active"><h3 style="color:var(--purple)">Theater</h3><div class="photo" style="background:linear-gradient(180deg,#fff,#8bd35a 35%,#2c2c2c 70%,#fff)" role="img" aria-label="Photo of a performer in green shirt and suspenders"></div><div class="bar" style="background:var(--purple)"></div></div>
    <div class="subject"><h3 style="color:var(--green)">Art</h3><div class="photo" style="background:linear-gradient(180deg,#fff,#c69a7a 35%,#b83a2c 65%,#e8e2dc)" role="img" aria-label="Photo of a child holding paintbrushes"></div><div class="bar" style="background:var(--green)"></div></div>
    <div class="subject"><h3 style="color:var(--orange)">Yoga</h3><div class="photo" style="background:linear-gradient(180deg,#fff,#d9b49a 45%,#9a9a9a 75%,#fff)" role="img" aria-label="Photo of a girl in a yoga pose"></div><div class="bar" style="background:var(--orange)"></div></div>
  </div>
  <div class="bubble-band" style="left:0;top:231px;width:343px;height:26px" role="img" aria-label="Colourful scalloped bubble border ornament"></div>
  <p class="blurb" style="left:30px;right:30px;top:266px">We are happy to arrange a trial lesson in all subjects we offer instruction in, just call us at <span class="link">(555) 010-4477</span><br>or <span class="link">email us</span> via the Contact page and we will find a day and time that is convenient for you.</p>
</section>

<!-- state 3: details open -->
<section class="screen" style="left:828px;top:571px;width:344px;height:285px;box-shadow:none;background:var(--panel)">
  <div class="play-band" role="img" aria-label="Blue banner with illustrated drum and electric guitar"></div>
  <h2 class="rule-heading play-title" style="top:43px">It's Time To Play!</h2>
  <div class="bubble-band" style="left:0;top:65px;width:344px;height:24px" role="img" aria-label="Colourful scalloped bubble border ornament"></div>
  <div class="play-panel">
    <div class="subject"><h3 style="color:var(--teal)">Music</h3><div class="photo" style="background:linear-gradient(180deg,#fff,#e6a08c 40%,#c86a3a 70%,#9ab0c8)" role="img" aria-label="Photo of a boy playing electric guitar"></div><div class="bar" style="background:var(--teal)"></div></div>
    <div class="subject active"><h3 style="color:var(--purple)">Theater</h3><div class="photo" style="height:44px;background:linear-gradient(180deg,#fff,#8bd35a 60%,#2c2c2c)" role="img" aria-label="Photo of a performer in green shirt and suspenders"></div>
      <div class="popup">Actors, we have something wonderful for you too! Bright Kestrel offers exciting acting workshops and personal coaching, all taught in students' homes, and offered in small groups or individually.</div></div>
    <div class="subject"><h3 style="color:var(--green)">Art</h3><div class="photo" style="background:linear-gradient(180deg,#fff,#c69a7a 35%,#b83a2c 65%,#e8e2dc)" role="img" aria-label="Photo of a child holding paintbrushes"></div><div class="bar" style="background:var(--green)"></div></div>
    <div class="subject"><h3 style="color:var(--orange)">Yoga</h3><div class="photo" style="background:linear-gradient(180deg,#fff,#d9b49a 45%,#9a9a9a 75%,#fff)" role="img" aria-label="Photo of a girl in a yoga pose"></div><div class="bar" style="background:var(--orange)"></div></div>
  </div>
  <div class="bubble-band" style="left:0;top:231px;width:344px;height:26px" role="img" aria-label="Colourful scalloped bubble border ornament"></div>
  <p class="blurb" style="left:30px;right:30px;top:266px">We are happy to arrange a trial lesson in all subjects we offer instruction in, just call us at <span class="link">(555) 010-4477</span><br>or <span class="link">email us</span> via the Contact page and we will find a day and time that is convenient for you.</p>
</section>

</body>
</html>
```